Letter Head for accounting firm

We need letter head designed using our attached logo.

We also need the following information on the letterhead:

482 E Mill Rd. Danvers, OH 43762

HarborLedgerLtd.com

1-855-613-2907

Contact Information for Business Card

Use logo

Colors

Designer to choose colors to be used in the design.

Requirements
Must have
• Business Card - Should also have name and title - email address

```html
<!DOCTYPE html>
<html lang="en">
<head>
<meta charset="utf-8">
<title>Harbor Ledger Group Ltd — Stationery Set</title>
<link rel="stylesheet" href="https://fonts.googleapis.com/css2?family=Roboto:wght@400;500;700&display=swap">
<style>
  :root {
    --stage: #7b7b7b;
    --paper: #ffffff;
    --brand-blue: #1b7ac2;
    --ink-dark: #222a33;
    --card-dark: #27303a;
    --text-body: #4a4f55;
    --text-contact: #333a40;
    --mark-faint-blue: #dbe6f3;
  }
  * { box-sizing: border-box; margin: 0; padding: 0; }
  html, body { width: 1200px; height: 1200px; overflow: hidden; }
  body {
    background: radial-gradient(circle at 50% 45%, #8a8a8a 0%, var(--stage) 70%);
    font-family: "Roboto", Arial, sans-serif;
    position: relative;
  }
  .piece {
    position: absolute;
    background: var(--paper);
    box-shadow: 0 2px 6px rgba(0,0,0,.35);
    overflow: hidden;
  }

  .brand { position: absolute; display: flex; flex-direction: column; align-items: center; }
  .brand-square { background: var(--brand-blue); }
  .brand-name {
    color: var(--brand-blue); font-weight: 700; text-transform: uppercase;
    white-space: nowrap; letter-spacing: .2px; text-align: center; line-height: 1.25;
  }

  .faint-mark { position: absolute; background: var(--mark-faint-blue); opacity: .55; }

  .footer-strip { position: absolute; left: 0; right: 0; bottom: 0; background: var(--ink-dark); }
  .footer-tab {
    position: absolute; right: 0; bottom: 0; background: var(--brand-blue);
    color: #fff; font-weight: 500; display: flex; align-items: center; justify-content: center;
    clip-path: polygon(12px 0, 100% 0, 100% 100%, 0 100%);
    white-space: nowrap;
  }

  .contact { position: absolute; color: var(--text-contact); line-height: 1.5; white-space: nowrap; }
  .contact b { font-weight: 700; color: var(--ink-dark); }

  /* letterhead */
  .letterhead { left: 64px; top: 36px; width: 539px; height: 761px; }
  .letterhead .brand { left: 30px; top: 30px; }
  .letterhead .brand-square { width: 50px; height: 50px; margin-bottom: 10px; }
  .letterhead .brand-name { font-size: 12px; }
  .letterhead .contact { right: 37px; top: 30px; text-align: right; font-size: 12px; line-height: 18px; }
  .letter-fields { position: absolute; left: 40px; top: 183px; font-size: 9.5px; font-weight: 700; color: var(--ink-dark); line-height: 18px; }
  .letter-body { position: absolute; left: 40px; top: 265px; width: 470px; font-size: 9.5px; color: var(--text-body); line-height: 13.5px; }
  .letter-body p { margin-bottom: 10px; }
  .letter-sign { position: absolute; left: 40px; top: 487px; font-size: 9.5px; font-weight: 700; color: var(--ink-dark); line-height: 13px; }
  .letter-sign .gap { height: 14px; }
  .letterhead .faint-mark { left: 250px; top: 392px; width: 280px; height: 300px; }
  .letterhead .footer-strip { height: 9px; }
  .letterhead .footer-tab { width: 210px; height: 24px; font-size: 13px; }

  /* business card front */
  .card-front { left: 620px; top: 36px; width: 523px; height: 327px; }
  .card-front .brand { left: 24px; top: 24px; }
  .card-front .brand-square { width: 34px; height: 34px; margin-bottom: 7px; }
  .card-front .brand-name { font-size: 11px; }
  .card-rule { position: absolute; left: 27px; top: 163px; width: 470px; height: 2px; background: var(--brand-blue); }
  .card-person { position: absolute; right: 27px; top: 132px; text-align: right; }
  .card-person .person-name { font-size: 18px; font-weight: 500; color: var(--ink-dark); line-height: 22px; }
  .card-person .person-title { font-size: 13px; color: var(--brand-blue); line-height: 24px; margin-top: 10px; }
  .card-front .contact { left: 28px; top: 208px; font-size: 13px; line-height: 18.5px; }
  .card-front .footer-strip { height: 8px; }
  .card-front .footer-tab { width: 205px; height: 22px; font-size: 13px; }

  /* business card back */
  .card-back { left: 620px; top: 382px; width: 523px; height: 328px; background: var(--card-dark); }
  .card-back .brand { left: 0; right: 0; top: 80px; }
  .card-back .brand-square { width: 80px; height: 80px; margin-bottom: 12px; }
  .card-back .brand-name { font-size: 17px; }
  .card-back .brand-rule { width: 225px; height: 1px; background: #c9ced4; margin-top: 6px; }
  .card-back .site { position: absolute; left: 0; right: 0; top: 246px; text-align: center; color: #e8ebee; font-size: 16px; }

  /* envelope back */
  .envelope-back { left: 64px; top: 815px; width: 521px; height: 265px; }
  .envelope-back .brand { left: 18px; top: 16px; }
  .envelope-back .brand-square { width: 30px; height: 30px; margin-bottom: 6px; }
  .envelope-back .brand-name { font-size: 9.5px; }
  .envelope-back .faint-mark { left: 345px; top: 20px; width: 150px; height: 150px; }
  .envelope-back .contact { left: 18px; top: 196px; font-size: 7.5px; line-height: 10px; }
  .envelope-back .footer-strip { height: 6px; }
  .envelope-back .footer-tab { width: 135px; height: 14px; font-size: 8px; clip-path: polygon(8px 0, 100% 0, 100% 100%, 0 100%); }

  /* envelope front with open flap */
  .envelope-front { left: 622px; top: 812px; width: 521px; height: 265px; }
  .envelope-flap { position: absolute; left: 0; top: 0; }
  .envelope-front .brand { left: 0; right: 0; top: 52px; }
  .envelope-front .brand-square { width: 38px; height: 38px; margin-bottom: 8px; }
  .envelope-front .brand-name { font-size: 12px; }
  .envelope-front .brand-rule { width: 120px; height: 1px; background: #9aa1a8; margin-top: 4px; }
  .envelope-front .site { position: absolute; left: 0; right: 0; top: 216px; text-align: center; font-size: 12.5px; color: var(--ink-dark); }
</style>
</head>
<body>

<section class="piece letterhead" aria-label="Letterhead">
  <div class="brand">
    <div class="brand-square"></div>
    <div class="brand-name">Harbor Ledger Group Ltd</div>
  </div>
  <div class="contact">
    <div><b>Tel:</b> 1-855-613-2907</div>
    <div><b>Fax:</b> 1-855-613-2907</div>
    <div><b>Email:</b> office@harborledgerltd.com</div>
    <div><b>Address:</b> 482 E Mill Rd.</div>
    <div>Danvers, OH 43762</div>
  </div>
  <div class="letter-fields">
    <div>Company Name:</div>
    <div>Address:</div>
    <div>City:</div>
    <div>Date:</div>
  </div>
  <div class="faint-mark"></div>
  <div class="letter-body">
    <p>Lorem Ipsum is simply dummy text of the printing and typesetting industry. Lorem Ipsum has been the industry's standard dummy text ever since the 1500s,</p>
    <p>When an unknown printer took a galley of type and scrambled it to make a type specimen book. It has survived not only five centuries, but also the leap into electronic typesetting, remaining essentially unchanged.</p>
    <p>It was popularised in the 1960s with the release of Transferline sheets containing Lorem Ipsum passages, and more recently with desktop publishing software like Pagewright Studio including versions of Lorem Ipsum.</p>
    <p>When an unknown printer took a galley of type and scrambled it to make a type specimen book. It has survived not only five centuries, but also the leap into electronic typesetting, remaining essentially unchanged.</p>
    <p>It was popularised in the 1960s with the release of Transferline sheets containing Lorem Ipsum passages, and more recently with desktop publishing software like Pagewright Studio including versions of Lorem Ipsum.</p>
  </div>
  <div class="letter-sign">
    <div>Sincerely,</div>
    <div class="gap"></div>
    <div>Name</div>
    <div>Designation</div>
  </div>
  <div class="footer-strip"></div>
  <div class="footer-tab">HarborLedgerLtd.com</div>
</section>

<section class="piece card-front" aria-label="Business card front">
  <div class="brand">
    <div class="brand-square"></div>
    <div class="brand-name">Harbor Ledger Group Ltd</div>
  </div>
  <div class="card-rule"></div>
  <div class="card-person">
    <div class="person-name">Your Name</div>
    <div class="person-title">Manager</div>
  </div>
  <div class="contact">
    <div><b>Tel:</b> 1-855-613-2907</div>
    <div><b>Fax:</b> 1-855-613-2907</div>
    <div><b>Email:</b> office@harborledgerltd.com</div>
    <div><b>Address:</b> 482 E Mill Rd.</div>
    <div>Danvers, OH 43762</div>
  </div>
  <div class="footer-strip"></div>
  <div class="footer-tab">www.harborledgerltd.com</div>
</section>

<section class="piece card-back" aria-label="Business card back">
  <div class="brand">
    <div class="brand-square"></div>
    <div class="brand-name">Harbor Ledger Group Ltd</div>
    <div class="brand-rule"></div>
  </div>
  <div class="site">HarborLedgerLtd.com</div>
</section>

<section class="piece envelope-back" aria-label="Envelope back">
  <div class="brand">
    <div class="brand-square"></div>
    <div class="brand-name">Harbor Ledger Group Ltd</div>
  </div>
  <div class="faint-mark"></div>
  <div class="contact">
    <div><b>Tel:</b> 1-855-613-2907</div>
    <div><b>Fax:</b> 1-855-613-2907</div>
    <div><b>Email:</b> office@harborledgerltd.com</div>
    <div><b>Address:</b> 482 E Mill Rd.</div>
    <div>Danvers, OH 43762</div>
  </div>
  <div class="footer-strip"></div>
  <div class="footer-tab">www.harborledgerltd.com</div>
</section>

<section class="piece envelope-front" aria-label="Envelope front">
  <svg class="envelope-flap" width="521" height="60" viewBox="0 0 521 60" aria-hidden="true">
    <polygon points="0,0 521,0 521,52 490,22 31,22 0,52" fill="#0d0d0d"/>
  </svg>
  <div class="brand">
    <div class="brand-square"></div>
    <div class="brand-name">Harbor Ledger Group Ltd</div>
    <div class="brand-rule"></div>
  </div>
  <div class="site">HarborLedgerLtd.com</div>
</section>

</body>
</html>
```